Wordpress Design for my Consulting Company

We want a WordPress site created for our new business. We have created a mock-up of the content we want on the site at https://marcusdellow.example-sites.com/website-5

We are not attached to any of the pictures and just put stock stuff from wix's editor, which we don't have rights to use outside of wix.

We are NOT looking to just port this site to WordPress, we are looking for some creative ways to display the content in a more professional artistic sense.

I have included several logo files and a text file with the colors and Fonts used in the logo. We are not looking to change the logo or the colors used in the logo.

The Schedule appointment links to a page that embeds a bookingnest.example.com calendar. https://bookingnest.example.com/marcus-dellow/brightvale

The final website domain will be enterprisebrightvale.example

Enterprise brightvale is a consulting company that works directly with the business owners and leaders of small businesses between 50-200 employees. We help companies make sure they have the right technology to meet their strategic goals. We are the anti-"Computer Guy" and we focus on business outcomes NOT cool technology gadgets.

The final design should communicate business growth and success.

Target Market(s)

Business Owners of companies with 50-200 employees

Coding

Coded - Design and coding required

Number of Pages Required

1 page

Font styles to use
Serif
Other font styles liked:
• Trajan Pro Bold, Open Sans

Requirements
Must have
• Should focus on consulting rather than technology.
• Should show the customer as the hero and we are just their guide.
• Must use the logo provided and the colors and fonts in the text file provided. Any other colors and fonts must be complementary.
• The design should scale for all devices computer, iPad, or phone
Should not have
• Should not focus on technology, we are the anti-"Computer Guy" and we focus on business outcomes NOT cool technology gadgets.

```html
<!DOCTYPE html>
<html lang="en">
<head>
<meta charset="utf-8">
<title>Enterprise Brightvale — Technology Advisors That Get Business</title>
<link rel="stylesheet" href="https://fonts.googleapis.com/css2?family=Cinzel:wght@400;600;700&family=Open+Sans:wght@400;600&display=swap">
<style>
:root{
  --accent:#c8784a;
  --accent-dark:#b36637;
  --ink:#1c1c1c;
  --text:#444;
  --muted:#777;
  --rule:#dcdcdc;
  --bar:#161616;
  --soft:#f2f2f2;
  --white:#fff;
}
*{box-sizing:border-box;margin:0;padding:0}
html,body{width:1200px;height:3403px;overflow:hidden}
body{position:relative;background:var(--white);font-family:"Open Sans",Arial,sans-serif;color:var(--text)}
.abs{position:absolute}
.serif{font-family:"Cinzel","Times New Roman",serif}
.hl{color:var(--accent)}
.btn{position:absolute;display:flex;align-items:center;justify-content:center;background:var(--accent);color:var(--white);font-family:"Open Sans",Arial,sans-serif;font-size:15px;font-weight:600;letter-spacing:.5px;border-radius:22px;text-transform:uppercase}
.section-title{position:absolute;left:0;width:1200px;text-align:center;font-family:"Cinzel",serif;font-weight:700;color:var(--ink);font-size:31px;letter-spacing:1px}
.title-rule{position:absolute;left:560px;width:80px;height:3px;background:linear-gradient(90deg,var(--ink) 50%,var(--accent) 50%)}

/* top bar */
.topbar{left:0;top:0;width:1200px;height:38px;background:var(--bar)}
.social-dot{position:absolute;top:7px;width:24px;height:24px;border:1px solid #777;border-radius:50%}
.topbar .btn{left:844px;top:0;width:218px;height:38px;border-radius:0;font-size:13px}

/* nav */
.nav{left:0;top:38px;width:1200px;height:87px;background:var(--white);box-shadow:0 2px 6px rgba(0,0,0,.08)}
.brand{position:absolute;left:140px;top:22px;display:flex;align-items:center;gap:14px}
.brand-mark{width:44px;height:44px;border-radius:50%;background:var(--accent)}
.brand-name{font-family:"Cinzel",serif;font-weight:700;font-size:22px;color:var(--ink);letter-spacing:1px}
.nav-link{position:absolute;top:40px;font-size:12px;letter-spacing:1px;color:#333}
.nav-link.active{color:var(--accent)}
.nav-active-bar{position:absolute;left:555px;top:109px;width:60px;height:16px;background:linear-gradient(180deg,transparent,#e8c4ad)}
.nav-sep{position:absolute;top:40px;width:1px;height:16px;background:#ccc}

/* hero */
.hero{left:0;top:125px;width:1200px;height:567px;background:linear-gradient(100deg,#8d8a86 0%,#d9d6d1 30%,#ecebe8 55%,#b9b3ab 80%,#6d655d 100%)}
.hero-title{position:absolute;left:0;top:160px;width:1200px;text-align:center;font-family:"Cinzel",serif;font-weight:700;font-size:46px;line-height:58px;color:var(--ink);letter-spacing:1px}
.hero-sub{position:absolute;left:0;top:290px;width:1200px;text-align:center;font-size:18px;color:#222}
.hero .btn{left:473px;top:345px;width:254px;height:46px}

/* do you know */
.dyk-item{position:absolute;top:834px;display:flex;align-items:center;gap:16px}
.dyk-icon{width:58px;height:58px;border:2px solid var(--accent);border-radius:50%;display:flex;align-items:center;justify-content:center}
.dyk-text{font-family:"Cinzel",serif;font-size:16px;line-height:20px;color:#333;letter-spacing:.5px}
.arrow{position:absolute;top:850px}

/* tired */
.tired{left:0;top:964px;width:1200px;height:517px;background:linear-gradient(90deg,#dedcd9 0%,#efefee 35%,#f3f3f3 65%,#e2e1df 100%)}
.tired-lead{position:absolute;left:250px;top:132px;width:700px;text-align:center;font-size:13px;line-height:22px;color:#555}
.orbit-item{position:absolute;font-size:12.5px;line-height:18px;color:#555;width:190px}
.orbit-item.left{text-align:right}
.orbit-icon{position:absolute;width:30px;height:30px;border:1.5px solid #666;border-radius:50%}
.orbit-dot{position:absolute;width:16px;height:16px;border:2px solid var(--accent);border-radius:50%;background:var(--white)}
.orbit-dot::after{content:"";position:absolute;left:3px;top:3px;width:6px;height:6px;border-radius:50%;background:var(--accent)}
.center-brand{position:absolute;left:450px;top:258px;width:300px;text-align:center}
.center-brand .brand-mark{margin:0 auto 12px;width:70px;height:70px}
.center-brand .brand-name{font-size:22px}

/* steps */
.step{position:absolute;top:1673px;width:240px;text-align:center}
.step-circle{width:114px;height:114px;margin:0 auto;border-radius:50%;background:#ededed;position:relative}
.step-circle.active{background:var(--white);border:3px solid var(--accent)}
.step-art{position:absolute;left:32px;top:32px;width:50px;height:50px;border-radius:8px;background:#c9c9c9}
.step-circle.active .step-art{background:#e6b99c;left:29px;top:29px}
.step-num{position:absolute;left:-4px;top:-2px;width:30px;height:30px;border-radius:50%;background:var(--ink);color:var(--white);font-size:15px;font-weight:600;display:flex;align-items:center;justify-content:center}
.step-name{margin-top:24px;font-family:"Cinzel",serif;font-weight:600;font-size:18px;color:var(--ink);letter-spacing:1px}
.step.active .step-name{color:var(--accent)}
.step-desc{margin:12px auto 0;width:200px;font-size:11.5px;line-height:18px;color:#555}
.dash-link{position:absolute;top:1712px}

/* mindset */
.mindset{left:0;top:2053px;width:1200px;height:378px;background:linear-gradient(180deg,#f3f3f3,#ececec)}
.mindset-title{position:absolute;left:0;top:72px;width:1200px;text-align:center;font-family:"Cinzel",serif;font-weight:700;font-size:27px;line-height:44px;color:var(--ink);letter-spacing:1px}
.mindset-text{position:absolute;left:260px;top:172px;width:680px;text-align:center;font-size:18px;line-height:30px;color:#222}
.mindset .btn{left:482px;top:258px;width:236px;height:42px}

/* testimonials */
.avatar{left:564px;top:2588px;width:72px;height:72px;border-radius:50%;background:radial-gradient(circle at 50% 45%,#c9a58e,#6f5648);border:3px solid var(--white);box-shadow:0 0 0 1px #ddd}
.t-arrow{position:absolute;top:2609px;width:30px;height:30px;border-radius:50%;display:flex;align-items:center;justify-content:center}
.quote{position:absolute;left:210px;top:2678px;width:780px;text-align:center;font-style:italic;font-size:15px;line-height:26px;color:#666}
.quote-mark{position:absolute;left:208px;top:2655px;font-family:Georgia,serif;font-size:90px;line-height:1;color:#e4e4e4}
.cite{position:absolute;left:0;top:2750px;width:1200px;text-align:center;font-family:"Cinzel",serif;font-size:17px;color:#333}

/* contact */
.contact{left:0;top:2835px;width:1200px;height:454px;background:var(--soft)}
.block-title{position:absolute;font-family:"Cinzel",serif;font-weight:700;font-size:27px;color:var(--ink);letter-spacing:1px}
.block-rule{position:absolute;width:80px;height:3px;background:linear-gradient(90deg,var(--ink) 50%,var(--accent) 50%)}
.field{position:absolute;background:var(--white);border:1px solid #e2e2e2;font-size:11px;color:#888;padding:10px 12px}
.contact .btn{left:143px;top:358px;width:114px;height:38px;font-size:14px}
.divider{position:absolute;left:687px;top:60px;width:1px;height:340px;background:#ddd}
.info{position:absolute;left:737px;display:flex;gap:18px;align-items:flex-start}
.info-icon{width:36px;height:36px;border-radius:50%;background:var(--accent);display:flex;align-items:center;justify-content:center;flex:none}
.info-label{font-size:12px;font-weight:600;color:var(--ink);letter-spacing:.5px}
.info-value{font-size:12px;line-height:20px;color:#555;margin-top:4px}
.follow{position:absolute;left:742px;top:363px;display:flex;align-items:center;gap:10px}
.follow span{font-family:"Cinzel",serif;font-size:20px;color:var(--ink);margin-right:10px;letter-spacing:1px}
.follow i{display:block;width:28px;height:28px;border-radius:50%;background:#2a5d9f}

/* footer */
.footer{left:0;top:3289px;width:1200px;height:72px;background:var(--bar)}
.footer-link{position:absolute;top:28px;font-family:"Cinzel",serif;font-size:15px;color:var(--white);letter-spacing:1px}
.copyright{left:0;top:3361px;width:1200px;height:42px;background:var(--accent);color:var(--white);font-size:13px;display:flex;align-items:center;justify-content:center}
</style>
</head>
<body>

<!-- top bar -->
<header class="abs topbar">
  <span class="social-dot" style="left:141px"></span>
  <span class="social-dot" style="left:169px"></span>
  <span class="social-dot" style="left:197px"></span>
  <a class="btn">Schedule Appointment</a>
</header>

<!-- navigation -->
<nav class="abs nav">
  <div class="brand"><span class="brand-mark"></span><span class="brand-name">Enterprise Brightvale</span></div>
  <span class="nav-link active" style="left:563px">HOME</span>
  <span class="nav-sep" style="left:630px"></span>
  <span class="nav-link" style="left:658px">HOW IT WORKS</span>
  <span class="nav-sep" style="left:777px"></span>
  <span class="nav-link" style="left:805px">TESTIMONIALS</span>
  <span class="nav-sep" style="left:925px"></span>
  <span class="nav-link" style="left:951px">CONTACT US</span>
</nav>
<div class="nav-active-bar"></div>

<!-- hero -->
<section class="abs hero" role="img" aria-label="Presenter leading a business strategy meeting in a bright conference room">
  <h1 class="hero-title">Technology Advisors That<br>“Get” Business.</h1>
  <p class="hero-sub">We help you leverage technology to create a competitive advantage.</p>
  <a class="btn">Schedule Appointment</a>
</section>

<!-- do you know -->
<h2 class="section-title" style="top:752px">Do You <span class="hl">Know</span></h2>
<div class="title-rule" style="top:803px"></div>
<svg class="arrow" style="left:94px" width="16" height="22" viewBox="0 0 16 22"><path d="M13 2 4 11l9 9" fill="none" stroke="#777" stroke-width="2.5"/></svg>
<svg class="arrow" style="left:1092px" width="16" height="22" viewBox="0 0 16 22"><path d="M3 2l9 9-9 9" fill="none" stroke="#333" stroke-width="2.5"/></svg>
<div class="dyk-item" style="left:140px">
  <span class="dyk-icon"><svg width="28" height="28" viewBox="0 0 28 28"><circle cx="14" cy="10" r="5" fill="none" stroke="#c8784a" stroke-width="2"/><path d="M5 25c1-6 5-9 9-9s8 3 9 9" fill="none" stroke="#c8784a" stroke-width="2"/></svg></span>
  <span class="dyk-text">We Get Standardizing<br>Customer Experience</span>
</div>
<div class="dyk-item" style="left:482px">
  <span class="dyk-icon" style="background:#f4e3d7"><svg width="28" height="28" viewBox="0 0 28 28"><circle cx="14" cy="15" r="9" fill="none" stroke="#c8784a" stroke-width="2"/><path d="M14 10v5l3 3" fill="none" stroke="#c8784a" stroke-width="2"/></svg></span>
  <span class="dyk-text">We Get Reducing Time<br>To Decision</span>
</div>
<div class="dyk-item" style="left:825px">
  <span class="dyk-icon"><svg width="28" height="28" viewBox="0 0 28 28"><rect x="5" y="7" width="18" height="16" rx="2" fill="none" stroke="#c8784a" stroke-width="2"/><path d="M5 12h18M10 4v5M18 4v5" stroke="#c8784a" stroke-width="2"/></svg></span>
  <span class="dyk-text">We Get Preparing<br>For Disruption</span>
</div>

<!-- tired of computer guys -->
<section class="abs tired" role="img" aria-label="Faded photo of a meeting audience behind the content">
  <h2 class="section-title" style="top:68px">Are You Tired of <span class="hl">“Computer Guys”</span> That...</h2>
  <div class="title-rule" style="top:118px"></div>
  <p class="tired-lead">Lorem ipsum dolor sit amet, consectetur adipiscing elit, sed do eiusmod tempor incididunt ut labore et dolore magna aliqua. Ut enim ad minim veniam, quis nostrud exercitation ullamco laboris nisi ut aliquip ex ea commodo consequat.</p>
  <svg class="abs" style="left:420px;top:156px" width="360" height="360" viewBox="0 0 360 360"><circle cx="180" cy="180" r="172" fill="none" stroke="#999" stroke-width="1.5" stroke-dasharray="2 5"/></svg>

  <p class="orbit-item left" style="left:222px;top:226px">Can’t explain how a technology will create business value, but insist it is necessary.</p>
  <span class="orbit-icon" style="left:424px;top:237px"></span><span class="orbit-dot" style="left:470px;top:243px"></span>
  <p class="orbit-item left" style="left:184px;top:326px">Say “No!” but do not give options on how to achieve your business outcome.</p>
  <span class="orbit-icon" style="left:382px;top:334px"></span><span class="orbit-dot" style="left:420px;top:340px"></span>
  <p class="orbit-item left" style="left:192px;top:432px">Don’t want to be involved in business strategy.</p>
  <span class="orbit-icon" style="left:392px;top:431px"></span><span class="orbit-dot" style="left:432px;top:437px"></span>

  <span class="orbit-dot" style="left:704px;top:232px"></span><span class="orbit-icon" style="left:738px;top:226px"></span>
  <p class="orbit-item" style="left:778px;top:226px">Give you the excuse, “You never asked.”</p>
  <span class="orbit-dot" style="left:762px;top:340px"></span><span class="orbit-icon" style="left:788px;top:334px"></span>
  <p class="orbit-item" style="left:828px;top:326px;width:200px">Recommend technology when a simple process or policy change would have the same effect.</p>
  <span class="orbit-dot" style="left:738px;top:448px"></span><span class="orbit-icon" style="left:774px;top:442px"></span>
  <p class="orbit-item" style="left:814px;top:432px;width:200px">Suggest expensive solutions that are just thrown away, soon after they are deployed.</p>

  <div class="center-brand"><div class="brand-mark"></div><div class="brand-name">Enterprise Brightvale</div></div>
  <a class="btn" style="left:483px;top:418px;width:234px;height:40px">Schedule Appointment</a>
</section>

<!-- four steps -->
<h2 class="section-title" style="top:1545px;line-height:40px">The <span class="hl">4 Steps</span> to Aligning Technology to<br>Your Business Strategy!</h2>
<div class="title-rule" style="top:1633px"></div>
<svg class="dash-link" style="left:300px" width="110" height="40" viewBox="0 0 110 40"><path d="M2 30c30 12 70 12 100-10" fill="none" stroke="#888" stroke-width="1.5" stroke-dasharray="4 4"/><path d="M96 16l7 3-4 7" fill="none" stroke="#888" stroke-width="1.5"/></svg>
<svg class="dash-link" style="left:555px" width="110" height="40" viewBox="0 0 110 40"><path d="M2 20c30-20 70-20 100 0" fill="none" stroke="#888" stroke-width="1.5" stroke-dasharray="4 4"/><path d="M96 14l7 6-7 4" fill="none" stroke="#888" stroke-width="1.5"/></svg>
<svg class="dash-link" style="left:810px" width="110" height="40" viewBox="0 0 110 40"><path d="M2 30c30 12 70 12 100-10" fill="none" stroke="#888" stroke-width="1.5" stroke-dasharray="4 4"/><path d="M96 16l7 3-4 7" fill="none" stroke="#888" stroke-width="1.5"/></svg>

<div class="step" style="left:100px">
  <div class="step-circle"><span class="step-art" role="img" aria-label="Telescope illustration"></span><span class="step-num">1</span></div>
  <div class="step-name">Discover</div>
  <p class="step-desc">Identify what is going on behind the scenes, and create a snapshot of the current infrastructure.</p>
</div>
<div class="step active" style="left:352px">
  <div class="step-circle active"><span class="step-art" role="img" aria-label="Presenter at a board illustration"></span><span class="step-num">2</span></div>
  <div class="step-name">Prioritize</div>
  <p class="step-desc">Meet to decide which solutions and policies will have the greatest impact on reaching the companies goals.</p>
</div>
<div class="step" style="left:606px">
  <div class="step-circle"><span class="step-art" role="img" aria-label="Checklist on a tablet illustration"></span><span class="step-num">3</span></div>
  <div class="step-name">Implement</div>
  <p class="step-desc">Implement those things that will give the greatest return on investment.</p>
</div>
<div class="step" style="left:860px">
  <div class="step-circle"><span class="step-art" role="img" aria-label="Wrench and screwdriver illustration"></span><span class="step-num">4</span></div>
  <div class="step-name">Maintain</div>
  <p class="step-desc">Create a system that keeps your technology aligned as strategy adjusts over time.</p>
</div>
<a class="btn" style="left:518px;top:1944px;width:164px;height:40px;background:#333">Get Started</a>

<!-- mindset -->
<section class="abs mindset">
  <h2 class="mindset-title">Computer guys frustrate business leaders because<br>they don’t have a business mindset.</h2>
  <p class="mindset-text">Brightvale advises on strategy that helps companies apply technology to gain a competitive advantage.</p>
  <a class="btn">Schedule Appointment</a>
</section>

<!-- testimonials -->
<h2 class="section-title" style="top:2492px">Client <span class="hl">Testimonials</span></h2>
<div class="title-rule" style="top:2544px"></div>
<span class="t-arrow" style="left:494px;background:#ccc"><svg width="10" height="12" viewBox="0 0 10 12"><path d="M7 1 2 6l5 5" fill="none" stroke="#fff" stroke-width="2"/></svg></span>
<div class="abs avatar" role="img" aria-label="Client portrait"></div>
<span class="t-arrow" style="left:674px;background:#e6a77e"><svg width="10" height="12" viewBox="0 0 10 12"><path d="M3 1l5 5-5 5" fill="none" stroke="#fff" stroke-width="2"/></svg></span>
<span class="quote-mark">“</span>
<p class="quote">Marcus and the team at Brightvale are in all our strategy meetings whether or not we think technology will be discussed. And, they have brought great insight to better let us meet our goals.</p>
<p class="cite"><span class="hl">– Dale Whitmore</span>, Cedar Ridge Fellowship</p>

<!-- contact -->
<section class="abs contact">
  <h2 class="block-title" style="left:143px;top:68px">Quick <span class="hl">Inquiry</span></h2>
  <div class="block-rule" style="left:143px;top:112px"></div>
  <div class="field" style="left:143px;top:143px;width:238px;height:39px">First Name</div>
  <div class="field" style="left:390px;top:143px;width:238px;height:39px">Last Name</div>
  <div class="field" style="left:143px;top:197px;width:238px;height:39px">Phone</div>
  <div class="field" style="left:390px;top:197px;width:238px;height:39px">Email</div>
  <div class="field" style="left:143px;top:245px;width:485px;height:91px">Message</div>
  <a class="btn">Submit</a>
  <div class="divider"></div>

  <h2 class="block-title" style="left:737px;top:68px">Contact <span class="hl">Details</span></h2>
  <div class="block-rule" style="left:737px;top:112px"></div>
  <div class="info" style="top:145px">
    <span class="info-icon"><svg width="16" height="20" viewBox="0 0 16 20"><path d="M8 1a6 6 0 0 0-6 6c0 5 6 12 6 12s6-7 6-12a6 6 0 0 0-6-6z" fill="#fff"/><circle cx="8" cy="7" r="2.2" fill="#c8784a"/></svg></span>
    <div><div class="info-label">ADDRESS</div><div class="info-value">1450 Linden Park Drive, Suite 200<br>Fairhaven, TX 77001</div></div>
  </div>
  <div class="info" style="top:235px">
    <span class="info-icon"><svg width="18" height="18" viewBox="0 0 18 18"><path d="M4 1l3 4-2 2c1 2 3 4 5 5l2-2 4 3-2 3C8 16 2 10 1 4z" fill="#fff"/></svg></span>
    <div><div class="info-label">PHONE</div><div class="info-value">(555) 014-2290</div></div>
  </div>
  <div class="info" style="top:300px">
    <span class="info-icon"><svg width="18" height="14" viewBox="0 0 18 14"><rect x="1" y="1" width="16" height="12" rx="1" fill="#fff"/><path d="M1 2l8 6 8-6" fill="none" stroke="#c8784a" stroke-width="1.5"/></svg></span>
    <div><div class="info-label">EMAIL</div><div class="info-value">mdellow@enterprisebrightvale.example</div></div>
  </div>
  <div class="follow"><span>Follow Us</span><i></i><i style="background:#2aa3e0"></i><i style="background:#0e76a8"></i></div>
</section>

<!-- footer -->
<footer class="abs footer">
  <span class="footer-link" style="left:305px">HOME</span>
  <span class="footer-link" style="left:420px">HOW IT WORKS</span>
  <span class="footer-link" style="left:610px">TESTIMONIALS</span>
  <span class="footer-link" style="left:790px">CONTACT US</span>
</footer>
<div class="abs copyright">©2018 by Enterprise Brightvale</div>

</body>
</html>
```